Steady Pathways, Inc
Steady Pathways
Bright & Fun-filled
Marisa Delacorte
P.O. Box 38216
4873-B Thimble Crest Road
Harlow Falls, NC 27845
madelacorte@steadypathwaysgrp.net
"Keep Moving Toward The Goal"
Logo File.

```html
<!DOCTYPE html>
<html lang="en">
<head>
<meta charset="utf-8">
<title>Steady Pathways, Inc — Stationery</title>
<link href="https://fonts.googleapis.com/css2?family=Nunito:wght@800&family=Open+Sans:wght@400;600;700&display=swap" rel="stylesheet">
<style>
  :root{
    --bg:#e8e3da;
    --paper:#ffffff;
    --ink:#333a45;
    --muted:#6b7380;
    --blue:#1d3f8f;
    --blue-light:#4a86c9;
    --accent:#f6c417;
    --card-dark:#111111;
    --faint:#edf1f6;
  }
  *{box-sizing:border-box;margin:0;padding:0}
  html,body{width:1200px;height:726px;overflow:hidden;background:var(--bg)}
  body{position:relative;font-family:"Open Sans",Arial,sans-serif;color:var(--ink)}
  .piece{position:absolute;background:var(--paper);overflow:hidden;box-shadow:0 2px 6px rgba(0,0,0,.18)}
  .footer-band{position:absolute;left:0;bottom:0;width:100%;background:var(--blue);border-top:3px solid var(--accent)}
  .brand{display:flex;align-items:center;gap:6px}
  .brand-dot{border-radius:50%;background:var(--blue);flex:none}
  .brand-name{font-family:"Nunito",Arial,sans-serif;font-weight:800;color:var(--blue);white-space:nowrap;line-height:1}
  .tagline{color:var(--blue-light);font-weight:600;white-space:nowrap}
  .address{position:absolute;text-align:right;color:var(--muted);line-height:1.35;font-style:normal}
  .backdrop-disc{position:absolute;border-radius:50%;background:var(--faint)}

  /* sheets */
  .sheet{top:142px;width:331px;height:465px}
  .sheet .brand{position:absolute;left:16px;top:22px}
  .sheet .brand-dot{width:14px;height:14px}
  .sheet .brand-name{font-size:16px}
  .sheet .tagline{position:absolute;left:16px;top:41px;font-size:6px}
  .sheet .address{right:16px;top:18px;font-size:5.5px}
  .sheet .backdrop-disc{width:120px;height:120px;left:105px;top:190px}
  .sheet .footer-band{height:30px}
  .fax-sheet{left:61px}
  .letter-sheet{left:416px}

  .fax-title{position:absolute;right:16px;top:92px;font-weight:700;font-size:15px;color:var(--ink)}
  .fax-table{position:absolute;left:16px;top:112px;width:299px;border-collapse:collapse;font-size:6px;color:var(--ink)}
  .fax-table td{border:0.8px solid #9aa0a8;height:13px;padding:0 3px}
  .fax-table td.label{width:22%}
  .fax-checks{position:absolute;left:16px;top:180px;width:299px;display:flex;justify-content:space-between;font-size:5.5px}
  .fax-checks span::before{content:"";display:inline-block;width:5px;height:5px;border:0.8px solid #777;margin-right:3px;vertical-align:-1px}

  /* business cards */
  .card{width:146px;height:82px}
  .card .footer-band{height:14px;border-top-width:2px}
  .card-front{left:911px;top:30px}
  .card-front .brand{position:absolute;left:8px;top:13px;gap:3px}
  .card-front .brand-dot{width:7px;height:7px}
  .card-front .brand-name{font-size:7px}
  .card-front .contact{position:absolute;right:8px;top:10px;text-align:right;font-size:4.5px;color:var(--muted);line-height:1.4}
  .card-front .contact strong{color:var(--blue);font-size:5px}
  .card-back{display:flex;align-items:center;justify-content:center}
  .card-back .brand{gap:4px}
  .card-back .brand-dot{width:10px;height:10px}
  .card-back .brand-name{font-size:10px}
  .card-back-dark{left:820px;top:127px;background:var(--card-dark)}
  .card-back-dark .brand-name{color:var(--paper)}
  .card-back-dark .brand-dot{background:var(--paper)}
  .card-back-light{left:987px;top:127px}

  /* envelopes */
  .envelope{left:789px;width:367px;height:174px}
  .envelope-back{top:230px}
  .envelope-back .flap{position:absolute;left:0;top:0;width:100%;height:22px;border-bottom:1px solid #d3d6dc}
  .envelope-back .brand{position:absolute;left:50%;top:28px;transform:translateX(-50%);gap:4px}
  .envelope-back .brand-dot{width:8px;height:8px}
  .envelope-back .brand-name{font-size:8px}
  .envelope-front{top:433px}
  .envelope-front .brand{position:absolute;left:14px;top:16px}
  .envelope-front .brand-dot{width:12px;height:12px}
  .envelope-front .brand-name{font-size:14px}
  .envelope-front .tagline{position:absolute;left:14px;top:33px;font-size:5.5px}
  .envelope-front .return{position:absolute;left:14px;top:50px;font-size:5px;color:var(--muted);line-height:1.4;font-style:normal}
  .envelope-front .backdrop-disc{width:100px;height:100px;right:24px;top:10px}
  .envelope-front .footer-band{height:18px;border-top-width:2px}
</style>
</head>
<body>

<section class="piece sheet fax-sheet" aria-label="Fax cover sheet">
  <div class="brand"><span class="brand-dot"></span><span class="brand-name">Steady Pathways</span></div>
  <p class="tagline">Keep Moving Toward The Goal</p>
  <address class="address">P.O. Box 38216<br>4873-B Thimble Crest Road<br>Harlow Falls, NC 27845<br>madelacorte@steadypathwaysgrp.net</address>
  <div class="backdrop-disc" aria-hidden="true"></div>
  <h2 class="fax-title">FAX</h2>
  <table class="fax-table">
    <tr><td class="label">To:</td><td></td><td class="label">From:</td><td></td></tr>
    <tr><td class="label">Fax:</td><td></td><td class="label">Pages:</td><td></td></tr>
    <tr><td class="label">Phone:</td><td></td><td class="label">Date:</td><td></td></tr>
    <tr><td class="label">Re:</td><td></td><td class="label">CC:</td><td></td></tr>
  </table>
  <div class="fax-checks"><span>Urgent</span><span>For Review</span><span>Please Comment</span><span>Please Reply</span><span>Please Recycle</span></div>
  <div class="footer-band"></div>
</section>

<section class="piece sheet letter-sheet" aria-label="Letterhead">
  <div class="brand"><span class="brand-dot"></span><span class="brand-name">Steady Pathways</span></div>
  <p class="tagline">Keep Moving Toward The Goal</p>
  <address class="address">P.O. Box 38216<br>4873-B Thimble Crest Road<br>Harlow Falls, NC 27845<br>madelacorte@steadypathwaysgrp.net</address>
  <div class="backdrop-disc" aria-hidden="true"></div>
  <div class="footer-band"></div>
</section>

<section class="piece card card-front" aria-label="Business card front">
  <div class="brand"><span class="brand-dot"></span><span class="brand-name">Steady Pathways</span></div>
  <p class="contact"><strong>Marisa Delacorte</strong><br>P.O. Box 38216<br>Harlow Falls, NC 27845</p>
  <div class="footer-band"></div>
</section>

<section class="piece card card-back card-back-dark" aria-label="Business card back, dark">
  <div class="brand"><span class="brand-dot"></span><span class="brand-name">Steady Pathways</span></div>
</section>
<section class="piece card card-back card-back-light" aria-label="Business card back, light">
  <div class="brand"><span class="brand-dot"></span><span class="brand-name">Steady Pathways</span></div>
</section>

<section class="piece envelope envelope-back" aria-label="Envelope back">
  <div class="flap"></div>
  <div class="brand"><span class="brand-dot"></span><span class="brand-name">Steady Pathways</span></div>
</section>

<section class="piece envelope envelope-front" aria-label="Envelope front">
  <div class="brand"><span class="brand-dot"></span><span class="brand-name">Steady Pathways</span></div>
  <p class="tagline">Keep Moving Toward The Goal</p>
  <address class="return">P.O. Box 38216<br>4873-B Thimble Crest Road<br>Harlow Falls, NC 27845</address>
  <div class="backdrop-disc" aria-hidden="true"></div>
  <div class="footer-band"></div>
</section>

</body>
</html>
```